Criação de Papelaria (6 itens) para Lumiar & Castelo
A empresa queria:
" EMPRESA FAMILIAR PRODUTORA DE GRÃOS hA 34 ANOS NO MERCADO, PIONEIRA EM IRRIGAÇÃO TIPO PIVO CENTRAL. "

```html
<!DOCTYPE html>
<html lang="pt-BR">
<head>
<meta charset="utf-8">
<title>Lumiar &amp; Castelo — Porta-copos</title>
<link rel="stylesheet" href="https://fonts.googleapis.com/css2?family=Marcellus&family=Fira+Sans:wght@400&display=swap">
<style>
  :root {
    --backdrop: #f1f1f1;
    --coaster-brown: #6c381b;
    --grain-dark: #7a3f1f;
    --grain-light: #a8673f;
    --accent-gold: #e2b262;
    --accent-beige: #c9a88a;
  }
  html, body {
    margin: 0;
    width: 1200px;
    height: 1200px;
    overflow: hidden;
    background: var(--backdrop);
  }
  .coaster {
    display: block;
    width: 1200px;
    height: 1200px;
  }
  .coaster-face { fill: var(--coaster-brown); }
  .coaster-ring { fill: none; stroke: var(--accent-gold); stroke-width: 5; }
  .grain-cluster { fill: url(#grain-tones); }
  .brand-dot { fill: var(--accent-beige); }
  .brand-name {
    font-family: "Marcellus", serif;
    font-size: 72px;
    fill: var(--accent-gold);
  }
  .contact-phone {
    font-family: "Fira Sans", sans-serif;
    font-size: 64px;
    fill: var(--accent-gold);
  }
  .contact-site {
    font-family: "Fira Sans", sans-serif;
    font-size: 27px;
    letter-spacing: 4px;
    fill: var(--accent-gold);
  }
</style>
</head>
<body>
<svg class="coaster" viewBox="0 0 1200 1200" xmlns="http://www.w3.org/2000/svg">
  <defs>
    <clipPath id="coaster-shape">
      <circle cx="600" cy="600" r="500"/>
    </clipPath>
    <radialGradient id="grain-tones" cx="0.55" cy="0.45" r="0.6">
      <stop offset="0" stop-color="var(--grain-light)"/>
      <stop offset="0.7" stop-color="var(--grain-dark)"/>
      <stop offset="1" stop-color="var(--coaster-brown)"/>
    </radialGradient>
  </defs>

  <circle class="coaster-face" cx="600" cy="600" r="500"/>

  <g clip-path="url(#coaster-shape)">
    <ellipse class="grain-cluster" cx="990" cy="470" rx="170" ry="290"
             role="img" aria-label="Ilustração de grãos empilhados"/>
  </g>

  <circle class="coaster-ring" cx="600" cy="600" r="470"/>

  <g class="brand">
    <circle class="brand-dot" cx="250" cy="500" r="38"/>
    <text class="brand-name" x="320" y="480">Lumiar &amp;</text>
    <text class="brand-name" x="320" y="560">Castelo</text>
  </g>

  <g class="contact">
    <text class="contact-phone" x="600" y="790" text-anchor="middle">(37) 98412-6630</text>
    <text class="contact-site" x="600" y="840" text-anchor="middle">www.lumiarcastelo.com.br</text>
  </g>
</svg>
</body>
</html>
```